Flyer Design Project

We are a restaurant meal delivery service. We deliver from a variety of restaurants. We would like a flyer that will promote our service to busy commuters. The flyer will be distributed at local train stations. I would like the flyer to say something like "What's for dinner?" or "Meet us at your place!" or anything that is catchy.
In the flyer we want the customer to order online at our website plateswiftly.com and use coupon code $5off. Using the coupon code will get them $5 off of their online purchase.
We would like to pass the flyers out in the morning and have the customers go online either on the train or at work to schedule the food to be delivered for dinner.
Target Market(s)
Hungry commuters that are in a rush 30 - 50 women
Industry/Entity Type
Restaurant

```html
<!DOCTYPE html>
<html lang="en">
<head>
<meta charset="utf-8">
<title>Plate Swiftly – Online Ordering Flyer</title>
<link href="https://fonts.googleapis.com/css2?family=Open+Sans:wght@400;600;700;800&display=swap" rel="stylesheet">
<style>
  :root{
    --brand-red:#b3202a;
    --text-dark:#3f3f3f;
    --pink:#e8247c;
    --blue:#1f7bc1;
    --green:#2eb34a;
    --bullet-red:#d2232a;
    --navy:#2a3590;
    --orange:#f26a21;
    --peach:#fde3c4;
    --cream:#fff6e8;
    --pill-grey:#cfcfcf;
    --ring:#c9cfc0;
    --white:#ffffff;
  }
  *{box-sizing:border-box;margin:0;padding:0}
  html,body{width:970px;height:1200px;overflow:hidden;background:#f2f2f2}
  body{font-family:"Open Sans",Arial,sans-serif;color:var(--text-dark)}
  .flyer{
    position:relative;width:970px;height:1200px;overflow:hidden;
    background:linear-gradient(to bottom,var(--white) 0%,var(--white) 52%,var(--cream) 68%,var(--peach) 84%,var(--white) 84%);
  }
  .abs{position:absolute}

  .brand-name{left:50px;top:250px;width:310px;font-weight:800;font-size:52px;line-height:1;color:var(--brand-red);letter-spacing:-1px}
  .brand-mark{left:150px;top:120px;width:110px;height:110px;border-radius:50%;background:var(--brand-red)}

  .food-photo{border-radius:50%;border:9px solid var(--ring);box-shadow:0 4px 10px rgba(0,0,0,.25)}
  .photo-salmon{left:359px;top:68px;width:300px;height:300px;background:radial-gradient(circle at 45% 45%,#e0622a,#b84117 45%,#6f8a2a 80%,#3b5e18)}
  .photo-steak{left:654px;top:193px;width:214px;height:214px;background:radial-gradient(circle at 45% 50%,#8c3318,#5a1d0e 55%,#c2571c 85%,#3a1208)}
  .photo-pizza{left:555px;top:316px;width:270px;height:270px;background:radial-gradient(circle at 50% 50%,#e7b04a,#d0662b 50%,#a73b1e 80%,#7a4b25)}

  .headline{left:55px;top:442px;font-size:52px;font-weight:600;color:var(--text-dark);letter-spacing:-.5px}

  .step{left:0;height:46px;border-radius:0 23px 23px 0;color:var(--white);font-weight:600;font-size:26px;line-height:46px;padding-left:56px}
  .step-select{top:496px;width:391px;background:var(--pink)}
  .step-choose{top:551px;width:534px;background:var(--blue)}
  .step-relax{top:605px;width:619px;background:var(--green);padding-left:24px}

  .terms{left:74px;top:703px;list-style:none;font-weight:600;font-size:21px;line-height:1.25;color:#2c2c2c}
  .terms li{position:relative;padding-left:34px;margin-bottom:8px}
  .terms li::before{content:"";position:absolute;left:0;top:7px;width:14px;height:14px;border-radius:50%;background:var(--bullet-red)}

  .addons-badge{left:457px;top:670px;width:150px;height:150px}
  .addons-label{left:467px;top:700px;width:130px;text-align:center;color:var(--white);font-size:36px;line-height:1;font-weight:400}
  .drink-cans{left:614px;top:628px;width:270px;height:165px;border-radius:14px;background:linear-gradient(90deg,#d9dadc,#c8d4cf 35%,#2f8a45 50%,#b71c22 75%,#e02a30)}

  .drinks{left:636px;top:822px;list-style:none;font-size:20px;line-height:30px;color:#2c2c2c}
  .drinks li{position:relative;padding-left:36px}
  .drinks li::before{content:"";position:absolute;left:0;top:9px;width:13px;height:13px;border-radius:50%;background:var(--bullet-red)}

  .supplies{left:46px;top:891px;width:371px;height:102px;border-radius:24px;background:var(--pill-grey);padding:12px 22px 0 22px}
  .supplies li{list-style:none;position:relative;display:flex;justify-content:space-between;font-size:15px;line-height:19px;padding-left:24px;color:#2c2c2c}
  .supplies li::before{content:"";position:absolute;left:0;top:5px;width:10px;height:10px;border-radius:50%;background:var(--bullet-red)}
  .supplies .price{font-weight:700;white-space:nowrap;padding-left:10px}

  .disclaimer{left:427px;top:885px;width:181px;height:111px;border-radius:12px;background:var(--bullet-red);color:var(--white);text-align:center;padding:12px 10px 0}
  .disclaimer h3{font-size:14px;font-weight:700;margin-bottom:8px}
  .disclaimer p{font-size:13px;line-height:17px;color:#ffd9d4}

  .web-band{left:0;top:1015px;width:970px;height:71px;background:var(--navy);color:var(--white)}
  .web-address{left:65px;top:12px;font-size:34px;font-weight:700;letter-spacing:2px}
  .coupon{left:494px;top:8px;font-size:20px;line-height:24px;font-weight:600}
  .coupon strong{font-size:27px;font-weight:800}

  .info-pill{left:51px;top:1091px;width:883px;height:80px;border-radius:40px;background:linear-gradient(to bottom,#f7962d,var(--orange))}
  .blank-oval{position:absolute;top:22px;height:36px;border-radius:18px;background:var(--white)}
  .oval-details{left:19px;width:159px}
  .oval-hours{left:683px;width:93px}
  .pill-label{position:absolute;top:20px;color:var(--white);font-size:27px;font-weight:400}
  .label-details{left:186px}
  .label-hours{left:788px}
  .cards{position:absolute;left:286px;top:11px;display:flex;gap:8px}
  .card{width:88px;height:58px;border-radius:4px;background:var(--white);border:2px solid #ddd;display:flex;align-items:center;justify-content:center;font-size:17px;font-weight:700;color:var(--navy)}
</style>
</head>
<body>
<main class="flyer">

  <div class="abs brand-name">Plate Swiftly</div>

  <div class="abs food-photo photo-salmon" role="img" aria-label="Photo of glazed salmon with rice and broccoli"></div>
  <div class="abs food-photo photo-steak" role="img" aria-label="Photo of grilled steak"></div>
  <div class="abs food-photo photo-pizza" role="img" aria-label="Photo of pizza with tomatoes and basil"></div>

  <h1 class="abs headline">Online Ordering</h1>

  <div class="abs step step-select">Select a Restaurant</div>
  <div class="abs step step-choose">Choose Delivery Time &amp; Items</div>
  <div class="abs step step-relax">RELAX! Your Meal will arrive as scheduled</div>

  <ul class="abs terms">
    <li>$15 Minimum Order</li>
    <li>Delivery $3.99</li>
    <li>Prices and menu items are subject<br>to change without notice</li>
    <li>All Credit Cards are accepted</li>
    <li>Company Checks OK</li>
  </ul>

  <svg class="abs addons-badge" viewBox="0 0 150 150" aria-hidden="true">
    <circle cx="75" cy="75" r="72" fill="#ffffff" stroke="#e2e2e2" stroke-width="2" stroke-dasharray="6 4"/>
    <circle cx="75" cy="75" r="60" fill="#c8202a"/>
  </svg>
  <div class="abs addons-label">Add<br>Ons</div>
  <div class="abs drink-cans" role="img" aria-label="Photo of three soda cans: diet cola, lemon-lime and cola"></div>

  <ul class="abs drinks">
    <li>Fizzco - 12oz.&nbsp; $0.75</li>
    <li>Fizzco - 6-pack&nbsp; $4.25</li>
    <li>Fizzco Diet - 12oz.&nbsp; $0.75</li>
    <li>Fizzco Diet - 6-pack $4.25</li>
    <li>Limora - 12oz.&nbsp; $0.75</li>
    <li>Limora- 6-pack.&nbsp; $4.25</li>
  </ul>

  <ul class="abs supplies">
    <li><span>Plates</span><span class="price">$.20 per</span></li>
    <li><span>Cups</span><span class="price">$.15 per</span></li>
    <li><span>Plastic ware - Includes knife, fork, spoon, napkin and salt &amp; pepper</span><span class="price">$.25 per</span></li>
  </ul>

  <div class="abs disclaimer">
    <h3>Plate Swiftly Disclaimer:</h3>
    <p>Food Photography<br>may not be affiliated<br>with any restaurant.</p>
  </div>

  <section class="abs web-band">
    <div class="abs web-address">plateswiftly.com</div>
    <div class="abs coupon">Using the coupon code will get them<br><strong>$5 off</strong> of their online purchase</div>
  </section>

  <section class="abs info-pill">
    <span class="blank-oval oval-details"></span>
    <span class="pill-label label-details">Details</span>
    <div class="cards">
      <div class="card">Vero</div>
      <div class="card">Maxicard</div>
      <div class="card">Dyscova</div>
      <div class="card">Amaro</div>
    </div>
    <span class="blank-oval oval-hours"></span>
    <span class="pill-label label-hours">Hours</span>
  </section>

</main>
</body>
</html>
```